Tandle Repair - Handyman and Home Repair Services

I need a business card/letterhead logo for my new handyman service in my local area. I'm happy for a logo design to be done prior to business card design so it can be incorporated on to the card, for which I'd be happy to pay more for. I'd like it to be modern and not using the typical pictures of tools and cartoon characters in dungarees! I like the idea of tools but in a more modern way i.e subtle background images in different shades to main colour. I do like the american retro designs and those that show age and patina for example, having an image half old, half new in its appearance to represent the repairing of things. Colours in mind are 1950's retro colours, ie using grey with pastel greens, red and cream. I'd like to break the mould and the stigma thats attached to these jobs and make it more cool and up to date. I hope this will attract interior designers and more modern businesses to use my services.

This is the logo design I like and would be happy for this idea and colours:

http://toast-a-roam.co.uk/wp-content/uploads/2011/01/t-r_logo600px.png

```html
<!DOCTYPE html>
<html lang="en">
<head>
<meta charset="utf-8">
<title>Tandle Repair – Business Card</title>
<link rel="stylesheet" href="https://fonts.googleapis.com/css2?family=Open+Sans:wght@400;600;700&display=swap">
<style>
  :root {
    --page-bg: #e9eaec;
    --card-top: #ffffff;
    --card-bottom: #e4e5e7;
    --brand-blue: #1f9ad6;
    --wave-light: #7fd0f3;
    --wave-dark: #2a9fd8;
    --wave-edge: #a9acb0;
    --text-dark: #3a3d42;
    --text-mid: #6b6f75;
  }
  html, body {
    margin: 0;
    width: 1200px;
    height: 900px;
    overflow: hidden;
    background: var(--page-bg);
    font-family: "Open Sans", sans-serif;
  }
  .canvas {
    position: relative;
    width: 1200px;
    height: 900px;
  }
  .card {
    position: absolute;
    left: 75px;
    top: 150px;
    width: 1050px;
    height: 600px;
    border-radius: 56px;
    overflow: hidden;
    background: radial-gradient(ellipse at 35% 30%, var(--card-top) 0%, var(--card-top) 35%, var(--card-bottom) 100%);
    box-shadow: 0 6px 24px rgba(0,0,0,0.12);
  }
  .card-wave {
    position: absolute;
    inset: 0;
  }
  .brand {
    position: absolute;
    left: 70px;
    top: 62px;
  }
  .brand-row {
    display: flex;
    align-items: center;
    gap: 18px;
  }
  .brand-mark {
    width: 46px;
    height: 46px;
    border-radius: 50%;
    background: var(--brand-blue);
  }
  .brand-name {
    font-size: 58px;
    font-weight: 700;
    color: var(--brand-blue);
    letter-spacing: 0.5px;
    line-height: 1;
  }
  .brand-tagline {
    margin: 10px 0 0 64px;
    font-size: 19px;
    color: var(--text-mid);
  }
  .person {
    position: absolute;
    left: 70px;
    top: 228px;
  }
  .person-name {
    font-size: 22px;
    font-weight: 600;
    color: var(--text-dark);
  }
  .person-role {
    font-size: 19px;
    color: var(--text-mid);
    margin-top: 2px;
  }
  .contact {
    position: absolute;
    left: 70px;
    top: 322px;
    list-style: none;
    margin: 0;
    padding: 0;
    font-size: 17px;
    color: var(--text-mid);
  }
  .contact li {
    display: flex;
    align-items: center;
    gap: 12px;
    height: 38px;
  }
  .contact-icon {
    width: 18px;
    height: 18px;
    fill: var(--text-dark);
  }
</style>
</head>
<body>
<div class="canvas">
  <section class="card">
    <svg class="card-wave" viewBox="0 0 1050 600" aria-hidden="true">
      <defs>
        <linearGradient id="waveFill" x1="0" y1="0" x2="1" y2="1">
          <stop offset="0" stop-color="var(--wave-light)"/>
          <stop offset="1" stop-color="var(--wave-dark)"/>
        </linearGradient>
      </defs>
      <path d="M1050 140 C 930 190, 880 300, 790 420 C 720 510, 640 570, 540 600 L 1050 600 Z" fill="var(--wave-edge)"/>
      <path d="M1050 160 C 950 210, 900 320, 815 430 C 750 515, 680 572, 585 600 L 1050 600 Z" fill="url(#waveFill)"/>
    </svg>

    <header class="brand">
      <div class="brand-row">
        <span class="brand-mark"></span>
        <span class="brand-name">Tandle Repair</span>
      </div>
      <div class="brand-tagline">Handyman and Home Repair Services</div>
    </header>

    <div class="person">
      <div class="person-name">Dr Owen Marsdale</div>
      <div class="person-role">Manager</div>
    </div>

    <ul class="contact">
      <li>
        <svg class="contact-icon" viewBox="0 0 24 24" aria-hidden="true"><path d="M6.6 10.8a15 15 0 0 0 6.6 6.6l2.2-2.2a1 1 0 0 1 1-.25 11.4 11.4 0 0 0 3.6.57 1 1 0 0 1 1 1V20a1 1 0 0 1-1 1A17 17 0 0 1 3 4a1 1 0 0 1 1-1h3.5a1 1 0 0 1 1 1c0 1.25.2 2.45.57 3.6a1 1 0 0 1-.25 1z"/></svg>
        <span>0161 555 0142</span>
      </li>
      <li>
        <svg class="contact-icon" viewBox="0 0 24 24" aria-hidden="true"><path d="M3 5h18a1 1 0 0 1 1 1v12a1 1 0 0 1-1 1H3a1 1 0 0 1-1-1V6a1 1 0 0 1 1-1zm9 7.5L20 7H4z"/></svg>
        <span>owen@tandlerepair.com</span>
      </li>
      <li>
        <span>Unit 3 Elm Court, Harwick HR4 2TD</span>
      </li>
    </ul>
  </section>
</div>
</body>
</html>
```